Business card for new small company called "ZU"

I need a Business Card for new company out of Sacramento called "ZU". It is a mindful executive leadership training and mentoring company. The name "ZU" comes from the verb to "ZU". But the "ZU" is also a little play on phraseology, because historically I have had engineer sort of business cards that read "Marta Dunsby, P.E." for Professional Engineer. Now I want to ZU marta dunsby ZU - all sort of run together as shown in the file.

I didn't design a logo because I just want something simple in caps "ZU". I would like all the content included in the attached PowerPoint file. I would like the "ZU" lettering to ZU more rounded than that shown. I'd like it to ZU fun in some way. I'd also would like the "ZU" to ZU an object within the business card that I could use on letterhead, etc. And I'd love to have the card in fonts that I could get from Word or PowerPower point for example. I'm not attached to the particular fonts I've picked. Rather I just want kind of fun, but not unprofessional. I'd ZU pleased to have a second side with just a ZU on it. I have a blue color in mind for the ZU and am kind of thinking a blue background with white print. But if you have better ideas, please offer them.
Oh. Also, I'd like the text to ZU editable in something like adobe illustrator in case I need to change any of the details like my email address.

Target Market(s)

Executives who want to feel more alive and ZU more effective at their work

Industry/Entity Type

Leadership

Contact Information for Business Card

Simple card with "ZU" as the logo immediately following my name.

Colors
0493ce
3176b5

Requirements
Must have
• "ZU" in fun yet professional lettering. Other text as show in the uploaded file.
Nice to have
• back side with catchy color or placement.
Should not have
• more than one color in addition to white. - Want simple one-color design.

```html
<!DOCTYPE html>
<html lang="en">
<head>
<meta charset="utf-8">
<title>ZU Business Card – Front and Back</title>
<link rel="stylesheet" href="https://fonts.googleapis.com/css2?family=Carlito:wght@400;700&display=swap">
<style>
  :root {
    --sheet: #ffffff;
    --card-blue: #3db5ff;
    --mark-pale: #b0f4ff;
    --mark-faint: #d8fbff;
    --frame-line: #aef0f4;
    --crop-blue: #2f7fe6;
    --name-blue: #2a80e8;
    --text-grey: #8c8c8c;
  }
  html, body {
    margin: 0;
    padding: 0;
    overflow: hidden;
    background: var(--sheet);
  }
  .sheet {
    position: relative;
    width: 1200px;
    height: 446px;
    overflow: hidden;
    background: var(--sheet);
    font-family: "Carlito", Calibri, Arial, sans-serif;
  }
  .crop-marks {
    position: absolute;
    inset: 0;
  }
  .crop-marks line {
    stroke: var(--crop-blue);
    stroke-width: 1.5;
  }
  .card {
    position: absolute;
    top: 106px;
    width: 462px;
    height: 298px;
    box-sizing: border-box;
    overflow: hidden;
  }
  .card--back {
    left: 42px;
    background: var(--card-blue);
  }
  .card--back .wordmark {
    position: absolute;
    left: 0;
    right: 0;
    top: 50px;
    text-align: center;
    font-weight: 700;
    font-size: 190px;
    line-height: 1;
    color: var(--mark-pale);
    letter-spacing: -3px;
  }
  .card--front {
    left: 696px;
    border: 2px solid var(--frame-line);
    background: var(--sheet);
  }
  .card--front .wordmark-faint {
    position: absolute;
    left: 14px;
    top: -12px;
    font-weight: 700;
    font-size: 180px;
    line-height: 1;
    color: var(--mark-faint);
    letter-spacing: -3px;
  }
  .contact {
    position: absolute;
    left: 260px;
    top: 86px;
  }
  .contact__name {
    margin: 0;
    font-size: 22px;
    font-weight: 700;
    line-height: 26px;
    color: var(--name-blue);
  }
  .contact__role {
    margin: 0 0 19px;
    font-size: 15px;
    line-height: 20px;
    color: var(--text-grey);
  }
  .contact__values {
    margin: 0 0 16px;
    padding: 0;
    list-style: none;
    color: var(--name-blue);
    font-size: 15px;
    line-height: 19px;
  }
  .contact__details {
    margin: 0;
    color: var(--text-grey);
    font-size: 15px;
    line-height: 19px;
  }
  .tagline {
    position: absolute;
    left: 14px;
    bottom: 9px;
    margin: 0;
    font-size: 11px;
    color: var(--text-grey);
  }
</style>
</head>
<body>
<main class="sheet">
  <svg class="crop-marks" width="1200" height="446" viewBox="0 0 1200 446" aria-hidden="true">
    <line x1="43" y1="68" x2="43" y2="94"/>
    <line x1="504" y1="68" x2="504" y2="94"/>
    <line x1="43" y1="416" x2="43" y2="440"/>
    <line x1="504" y1="416" x2="504" y2="440"/>
    <line x1="6" y1="106" x2="34" y2="106"/>
    <line x1="6" y1="404" x2="34" y2="404"/>
    <line x1="516" y1="106" x2="542" y2="106"/>
    <line x1="516" y1="404" x2="542" y2="404"/>
    <line x1="696" y1="68" x2="696" y2="94"/>
    <line x1="1157" y1="68" x2="1157" y2="94"/>
    <line x1="696" y1="416" x2="696" y2="440"/>
    <line x1="1157" y1="416" x2="1157" y2="440"/>
    <line x1="659" y1="106" x2="686" y2="106"/>
    <line x1="659" y1="404" x2="686" y2="404"/>
    <line x1="1170" y1="106" x2="1196" y2="106"/>
    <line x1="1170" y1="404" x2="1196" y2="404"/>
  </svg>

  <section class="card card--back" aria-label="Card back">
    <span class="wordmark">ZU</span>
  </section>

  <section class="card card--front" aria-label="Card front">
    <span class="wordmark-faint" aria-hidden="true">ZU</span>
    <div class="contact">
      <h1 class="contact__name">Marta Dunsby</h1>
      <p class="contact__role">Founder, Seeker</p>
      <ul class="contact__values">
        <li>Know yourself</li>
        <li>Have fun</li>
        <li>Change the world</li>
      </ul>
      <p class="contact__details">(916) 555-0148<br>martadunsby@zufunlearn.com</p>
    </div>
    <p class="tagline">An Unlimited Partnership</p>
  </section>
</main>
</body>
</html>
```